Meridel Haulage - Website

A clean, not cluttered informative website for our business. We specialize in the transportation of radioactive materials across North America. The site is mostly for information about our company and will not be used to attract business but will be used to attract employee's mainly drivers. Driver's are very hard to find in our area. One of the pages needs to be a job's posting page with an apply now button. Either an application can be filled out there or a resume can be uploaded which ever functionality works better. I would like a website that I can easily edit, ability to change text and photos.

Number of Pages Required

5+ page

Colors

Designer to choose colors to be used in the design.

Requirements
Must have
• Home - About - Services - Jobs - Contact pages
• A way prospective employee's can apply or upload their resume to be emailed to me
• Very clean apperance
Should not have
• I don't want it to be busy

```html
<!DOCTYPE html>
<html lang="en">
<head>
<meta charset="utf-8">
<title>Meridel Haulage</title>
<link href="https://fonts.googleapis.com/css2?family=Rubik:ital,wght@0,300;0,400;0,500;0,700;0,800;1,300;1,400&display=swap" rel="stylesheet">
<style>
:root{
  --navy:#141b2d;
  --navy-soft:#1d2539;
  --orange:#f47b20;
  --paper:#f7f7f7;
  --white:#ffffff;
  --ink:#111111;
  --muted:#8a8a8a;
  --line:#c9c9c9;
}
*{margin:0;padding:0;box-sizing:border-box}
html,body{width:1200px;height:4107px;overflow:hidden}
body{position:relative;background:var(--paper);font-family:"Rubik",sans-serif;color:var(--ink)}
.abs{position:absolute}
.photo{position:absolute}

/* hero */
.hero-panel{left:0;top:0;width:600px;height:734px;background:var(--navy)}
.hero-photo{left:101px;top:77px;width:1000px;height:581px;background:linear-gradient(90deg,#3a3a38 0%,#4e4a42 45%,#a88a5e 60%,#c49a62 80%,#8c7a4e 100%)}
.hero-shade{left:101px;top:77px;width:499px;height:581px;background:rgba(20,27,45,.55)}
.top-phone{right:99px;top:30px;font-size:14px;color:var(--ink)}
.hero-title{left:184px;top:212px;font-weight:300;font-size:66px;line-height:70px;color:var(--white);letter-spacing:1px}
.hero-text{left:184px;top:382px;width:340px;font-size:13px;line-height:16px;color:var(--white)}
.btn{position:absolute;background:var(--orange);color:var(--white);font-size:13px;display:flex;align-items:center;justify-content:center;gap:22px}
.hero-btn{left:184px;top:455px;width:238px;height:49px}
.nav{position:absolute;display:flex;font-size:13px;font-weight:500;color:var(--white)}
.nav span{position:absolute;white-space:nowrap}
.hero-nav{left:0;top:688px}

/* brand */
.brand{left:652px;top:748px;width:412px;display:flex;align-items:center;gap:16px;font-weight:700;font-size:42px;color:var(--orange)}
.brand i{display:block;width:22px;height:22px;background:var(--orange)}

/* about */
.section-title{position:absolute;font-weight:800;font-size:44px;letter-spacing:1px;color:var(--ink)}
.about-title{left:99px;top:810px}
.tab-title{position:absolute;font-style:italic;font-weight:300;font-size:16px;line-height:20px;color:var(--muted)}
.tab-title.active{font-style:normal;font-weight:400;color:var(--ink);left:153px}
.about-photo{left:397px;top:907px;width:704px;height:337px;background:linear-gradient(180deg,#b9c1c7 0%,#8d949a 45%,#4a4f55 75%,#5a5a58 100%)}
.about-sub{left:397px;top:1290px;font-size:19px;font-weight:500;letter-spacing:1px}
.note{right:99px;top:1294px;font-size:13px}
.about-text{left:397px;top:1343px;width:400px;font-size:12.5px;line-height:16px;color:#333}
.link-btn{left:893px;top:1378px;width:208px;height:47px;font-size:12px}

/* options */
.options{left:0;top:1500px;width:1200px;height:555px;background:#f3f3f3}
.opt{position:absolute;width:240px}
.opt-num{font-weight:300;font-size:42px;line-height:46px}
.opt-title{margin-top:16px;font-style:italic;font-size:14px;line-height:16px;color:#333}
.opt-text{margin-top:12px;font-size:11.5px;line-height:15px;color:var(--muted)}

/* services */
.services-title{left:99px;top:2117px}
.svc-tab{position:absolute;top:2214px;font-size:12px;color:var(--muted)}
.svc-tab.active{color:var(--ink)}
.svc-underline{left:99px;top:2240px;width:100px;height:2px;background:var(--ink)}
.svc-rule{left:99px;top:2241px;width:1002px;height:1px;background:#e2e2e2}
.svc-col{position:absolute;top:2282px;height:447px}
.svc-head{position:absolute;left:22px;top:22px;font-size:14px;line-height:18px;color:var(--white)}
.svc-vert{position:absolute;left:18px;bottom:14px;font-size:12px;color:var(--white);transform:rotate(-90deg);transform-origin:left bottom;white-space:nowrap;translate:14px 0}

/* employment */
.jobs-panel{left:0;top:2822px;width:600px;height:603px;background:var(--navy)}
.jobs-photo{left:600px;top:2822px;width:600px;height:603px;background:linear-gradient(120deg,#3a3632 0%,#6b5f52 35%,#e6dfd6 70%,#ffffff 100%)}
.jobs-title{left:99px;top:2878px;font-weight:800;font-size:44px;line-height:44px;color:var(--white);letter-spacing:1px}
.jobs-lead{left:99px;top:2980px;font-size:14px;color:var(--white)}
.field{position:absolute;left:99px;width:424px;border-bottom:1px solid #8a91a3;font-style:italic;font-size:13px;color:var(--white);padding-bottom:10px}
.send-btn{left:99px;top:3260px;width:424px;height:55px;font-size:14px}
.req{left:99px;top:3328px;font-size:11.5px;color:var(--white)}

/* contact */
.contact-title{left:99px;top:3497px}
.card{left:268px;top:3617px;width:664px;height:211px;background:var(--white)}
.card-head{left:312px;top:3648px;font-size:14px;font-weight:500}
.card-lines{left:312px;top:3682px;font-size:12px;line-height:16px;color:var(--muted)}
.dots{left:488px;top:3861px;display:flex;gap:10px}
.dots i{display:block;width:48px;height:3px;background:#dcdcdc}
.dots i:first-child{background:var(--ink)}

/* footer */
.footer{left:0;top:3940px;width:1200px;height:167px;background:var(--navy)}
.rights{left:1008px;top:4009px;font-size:13px;color:var(--white)}
</style>
</head>
<body>

<header>
  <div class="abs hero-panel"></div>
  <div class="photo hero-photo" role="img" aria-label="Tractor-trailer truck driving on a highway at sunset"></div>
  <div class="abs hero-shade"></div>
  <div class="abs top-phone">contact phone number</div>
  <h1 class="abs hero-title">LOREM<br>IPSUM</h1>
  <p class="abs hero-text">Lorem ipsum dolor sit amet, consectetur adipiscing elit, sed do eiusmod tempor incididunt ut labore</p>
  <a class="btn hero-btn">Contact us
    <svg width="50" height="10" viewBox="0 0 50 10"><path d="M0 5h48M43 1l5 4-5 4" stroke="#fff" stroke-width="1.5" fill="none"/></svg>
  </a>
  <nav class="nav hero-nav">
    <span style="left:145px">HOME</span><span style="left:214px">ABOUT US</span><span style="left:310px">SERVICES</span><span style="left:405px">JOBS</span><span style="left:471px">CONTACT US</span>
  </nav>
</header>

<div class="abs brand"><i></i>Meridel Haulage</div>

<section class="about">
  <h2 class="section-title about-title">ABOUT US</h2>
  <div class="tab-title" style="left:99px;top:908px">Title number<br>one</div>
  <div class="tab-title active" style="top:1032px">Title number<br>two</div>
  <div class="tab-title" style="left:99px;top:1155px">Title number<br>three</div>
  <div class="tab-title" style="left:99px;top:1280px">Title number four</div>
  <div class="tab-title" style="left:99px;top:1404px">Title number five</div>
  <div class="photo about-photo" role="img" aria-label="Truck hauling cylindrical tanks on a flatbed trailer"></div>
  <h3 class="abs about-sub">TITLE NUMBER TWO</h3>
  <div class="abs note">note 1</div>
  <p class="abs about-text">Lorem ipsum dolor sit amet, consectetur adipiscing elit, sed do eiusmod tempor incididunt ut labore et dolore magna aliqua. Ut enim ad minim veniam, quis nostrud exercitation ullamco laboris nisi ut aliquip ex ea commodo consequat. Duis aute irure dolor in reprehenderit in voluptate velit esse cillum dolore eu fugiat nulla pariatur.</p>
  <a class="btn link-btn">LINK</a>
</section>

<section class="abs options">
  <div class="opt" style="left:99px;top:100px"><div class="opt-num">01</div><div class="opt-title">FIRST OPTION<br>TITLE</div><p class="opt-text">Lorem ipsum dolor sit amet, consectetur adipiscing elit, sed do eiusmod tempor incididunt ut labore et dolore magna aliqua. Ut enim ad minim veniam, quis nostrud exercitation ullamco laboris nisi ut aliquip ex ea commodo consequat.</p></div>
  <div class="opt" style="left:353px;top:242px"><div class="opt-num">02</div><div class="opt-title">SECOND OPTION<br>TITLE</div><p class="opt-text">Lorem ipsum dolor sit amet, consectetur adipiscing elit, sed do eiusmod tempor incididunt ut labore et dolore magna aliqua. Ut enim ad minim veniam, quis nostrud exercitation ullamco laboris nisi ut aliquip ex ea commodo consequat.</p></div>
  <div class="opt" style="left:608px;top:100px"><div class="opt-num">03</div><div class="opt-title">THIRD OPTION<br>TITLE</div><p class="opt-text">Lorem ipsum dolor sit amet, consectetur adipiscing elit, sed do eiusmod tempor incididunt ut labore et dolore magna aliqua. Ut enim ad minim veniam, quis nostrud exercitation ullamco laboris nisi ut aliquip ex ea commodo consequat.</p></div>
  <div class="opt" style="left:860px;top:242px"><div class="opt-num">04</div><div class="opt-title">FOURTH OPTION<br>TITLE</div><p class="opt-text">Lorem ipsum dolor sit amet, consectetur adipiscing elit, sed do eiusmod tempor incididunt ut labore et dolore magna aliqua. Ut enim ad minim veniam, quis nostrud exercitation ullamco laboris nisi ut aliquip ex ea commodo consequat.</p></div>
</section>

<section class="services">
  <h2 class="section-title services-title">OUR SERVICES</h2>
  <div class="abs svc-rule"></div>
  <div class="svc-tab active" style="left:99px">Service 1</div>
  <div class="svc-tab" style="left:288px">Service 2</div>
  <div class="svc-tab" style="left:515px">Service 3</div>
  <div class="abs svc-underline"></div>
  <div class="svc-col" style="left:99px;width:230px;background:linear-gradient(180deg,#2a3346,#1c2333)" role="img" aria-label="Dark-toned truck at a loading yard">
    <div class="svc-head">Enter text about<br>«Service 1»</div><div class="svc-vert">About 1</div>
  </div>
  <div class="svc-col" style="left:329px;width:318px;background:linear-gradient(180deg,#bcc7c4 0%,#c58a78 45%,#5e6469 100%)" role="img" aria-label="Truck with a shipping container on the road"></div>
  <div class="svc-col" style="left:647px;width:224px;background:linear-gradient(180deg,#3c4152,#232838)" role="img" aria-label="City skyline above a rail yard at dusk">
    <div class="svc-head">Enter text about<br>«Service 2»</div><div class="svc-vert">About 2</div>
  </div>
  <div class="svc-col" style="left:871px;width:230px;background:linear-gradient(180deg,#1f2535,#4b5264 70%,#2a3040)" role="img" aria-label="Highway light trails at night">
    <div class="svc-head">Enter text about<br>«Service 3»</div><div class="svc-vert">About 3</div>
  </div>
</section>

<section class="jobs">
  <div class="abs jobs-panel"></div>
  <div class="photo jobs-photo" role="img" aria-label="Driver's hands on a truck steering wheel in sunlight"></div>
  <h2 class="abs jobs-title">EMPLOYMENT<br>OPPORTUNITIES</h2>
  <p class="abs jobs-lead">Interested in joining our team?</p>
  <div class="field" style="top:3052px">Name</div>
  <div class="field" style="top:3120px">Email</div>
  <div class="field" style="top:3189px">Upload resume file</div>
  <a class="btn send-btn">Send</a>
  <p class="abs req">Resume file requirements: (PDF, MS Word)</p>
</section>

<section class="contact">
  <h2 class="section-title contact-title">CONTACT</h2>
  <div class="photo" style="left:0;top:3639px;width:216px;height:161px;background:linear-gradient(180deg,#5a2a18,#c4622a 60%,#2a1a14)" role="img" aria-label="Port cranes at sunset"></div>
  <div class="abs card"></div>
  <div class="abs card-head">Contact us</div>
  <div class="abs card-lines">Address line<br>Phone number<br>Company info</div>
  <div class="photo" style="left:696px;top:3639px;width:214px;height:170px;background:linear-gradient(135deg,#c9683a,#4a7c8c 50%,#d8a048)" role="img" aria-label="Stacked shipping containers"></div>
  <div class="photo" style="left:981px;top:3639px;width:219px;height:161px;background:linear-gradient(180deg,#8d9aa3,#5d666c 60%,#3d4246)" role="img" aria-label="Trucks on a multi-lane highway"></div>
  <div class="abs dots"><i></i><i></i><i></i><i></i></div>
</section>

<footer>
  <div class="abs footer"></div>
  <nav class="nav" style="left:0;top:4009px">
    <span style="left:115px">HOME</span><span style="left:184px">ABOUT US</span><span style="left:280px">SERVICES</span><span style="left:375px">JOBS</span><span style="left:441px">CONTACT US</span>
  </nav>
  <div class="abs rights">all rights reserved</div>
</footer>

</body>
</html>
```